Velmor Agritech, Inc. Business Card

We are joint venture hybrid vegetable seed company. We design & breed application specific products for fresh market and processing applications. We are looking for a business card that will have impact and convey elegance, excellence, high technology, and have enormous eye appeal. It needs to be unique in design and can incorporate photos, or symbols as the case may be.

I very much enjoy the minimalist approach to Quorlin's product designs. We would like to include a tag line in the business card: Breeding Success

Target Market(s)

We breed proprietary products that provide better solutions for growers, harvesters, packers, shippers, wholesalers, retailers, consumers, and processors. Regional seed distributors worldwide are our primary clients and then growers. We need to appeal first and foremost to the distributors who will be representing us and selling the products in their target markets.

Industry/Entity Type

Business

Requirements
Must have
• It will have a picture of a cluster of tomatoes on one side and the other side will include the logo, a tag line, our contact information, and a possibly a picture or symbol. I want the contact side to be edgy and convey elegance, solidity, and exclusivity.
Nice to have
• Surprise us with something special.
Should not have
• Card needs to work well with the green logo so it can't be diminished by the background color of the card.

```html
<!DOCTYPE html>
<html lang="en">
<head>
<meta charset="utf-8">
<title>Velmor Agritech, Inc. — Business Card</title>
<link rel="stylesheet" href="https://fonts.googleapis.com/css2?family=Playfair+Display:ital,wght@1,700;1,900&family=Oswald:wght@300;400&display=swap">
<style>
  :root {
    --photo-dark: #3a3a3a;
    --photo-mid: #8a8a8a;
    --photo-light: #c9c9c9;
    --tomato: #d9261c;
    --panel: #d4d4d4;
    --ink: #1c1c1c;
    --brand-red: #d7202a;
    --muted: #8a8a8a;
    --ghost: #e0e0e0;
    --accent-yellow: #fff200;
    --frame: #e6e6e6;
  }
  html, body {
    margin: 0;
    padding: 0;
    width: 1200px;
    height: 343px;
    overflow: hidden;
    background: #ffffff;
  }
  .card {
    position: relative;
    width: 1200px;
    height: 343px;
    overflow: hidden;
  }
  .card__photo-side {
    position: absolute;
    left: 0;
    top: 0;
    width: 600px;
    height: 343px;
    background:
      radial-gradient(ellipse 130px 165px at 300px 170px, var(--tomato) 0%, var(--tomato) 55%, rgba(217,38,28,0) 100%),
      linear-gradient(90deg, var(--photo-dark) 0%, var(--photo-mid) 45%, var(--photo-light) 60%, var(--photo-dark) 100%);
  }
  .card__frame {
    position: absolute;
    left: 0;
    top: 0;
  }
  .card__info-side {
    position: absolute;
    left: 600px;
    top: 0;
    width: 600px;
    height: 343px;
    background: var(--panel);
    overflow: hidden;
  }
  .ghost-word {
    position: absolute;
    font-family: "Playfair Display", serif;
    font-style: italic;
    font-weight: 700;
    color: var(--ghost);
    white-space: nowrap;
    line-height: 1;
  }
  .ghost-word--breeding { left: -40px; top: -28px; font-size: 110px; }
  .ghost-word--success { left: 150px; top: 104px; font-size: 118px; }
  .tagline {
    position: absolute;
    margin: 0;
    font-family: "Playfair Display", serif;
    font-style: italic;
    font-weight: 900;
    line-height: 1;
    white-space: nowrap;
    letter-spacing: -1px;
  }
  .tagline__first { left: 38px; top: 74px; font-size: 76px; color: var(--ink); }
  .tagline__second { left: 162px; top: 131px; font-size: 76px; color: var(--brand-red); }
  .divider { position: absolute; left: 36px; top: 242px; }
  .contact-person {
    position: absolute;
    left: 38px;
    top: 257px;
    font-family: "Oswald", sans-serif;
  }
  .contact-person__name { font-size: 12.5px; font-weight: 400; color: var(--ink); letter-spacing: 0.2px; }
  .contact-person__role { font-size: 10.5px; font-weight: 300; color: var(--muted); margin-top: 1px; }
  .contact-address {
    position: absolute;
    right: 184px;
    top: 256px;
    font-family: "Oswald", sans-serif;
    font-size: 10.5px;
    font-weight: 400;
    line-height: 14.5px;
    text-align: right;
    color: var(--ink);
    font-style: normal;
  }
  .contact-address__phone { color: var(--muted); font-weight: 300; }
  .brand-badge {
    position: absolute;
    left: 488px;
    top: 36px;
    width: 88px;
    height: 88px;
    border-radius: 50%;
    background: var(--accent-yellow);
    display: flex;
    align-items: center;
    justify-content: center;
    text-align: center;
    font-family: "Oswald", sans-serif;
    font-weight: 400;
    font-size: 11px;
    line-height: 13px;
    color: var(--ink);
  }
</style>
</head>
<body>
  <main class="card">
    <section class="card__photo-side" role="img" aria-label="Photograph of a cluster of ripe red vine tomatoes against a desaturated greenhouse background"></section>
    <svg class="card__frame" width="600" height="343" viewBox="0 0 600 343" aria-hidden="true">
      <polyline points="168,26 28,26 28,318 168,318" fill="none" stroke="var(--frame)" stroke-width="2"/>
      <polyline points="440,26 572,26 572,318 440,318" fill="none" stroke="var(--frame)" stroke-width="2"/>
    </svg>

    <section class="card__info-side">
      <span class="ghost-word ghost-word--breeding" aria-hidden="true">eding</span>
      <span class="ghost-word ghost-word--success" aria-hidden="true">Success</span>

      <h1 class="tagline tagline__first">Breeding</h1>
      <p class="tagline tagline__second">Success</p>

      <svg class="divider" width="384" height="8" viewBox="0 0 384 8" aria-hidden="true">
        <circle cx="3" cy="4" r="2.5" fill="var(--ink)"/>
        <line x1="7" y1="4" x2="377" y2="4" stroke="var(--muted)" stroke-width="1" stroke-dasharray="1.5 2"/>
        <circle cx="381" cy="4" r="2.5" fill="var(--ink)"/>
      </svg>

      <div class="contact-person">
        <div class="contact-person__name">MAREK TOLLAN</div>
        <div class="contact-person__role">Executing Manager</div>
      </div>

      <address class="contact-address">
        48 - LARCH STREET, B/14-TERRACE<br>
        BUILDING 560032- PUNE, INDIA<br>
        <span class="contact-address__phone">Ph. 001-30918846, Fax-001-30918847</span>
      </address>

      <div class="brand-badge">Velmor<br>Agritech, Inc.</div>
    </section>
  </main>
</body>
</html>
```